"Aviation Law Firm Needs Banner for Fly-In Website"

My firm is looking for a web banner which will be advertised on www.kestrel-meet.org. The banner is going to be used for advertisement leading up to the big fly-in event being held in April.

My law firm represents pilots, plane owners, airlines, and anyone else that has an interest in aviation.

I would like to see some animation if possible, which would include aviation/cutting edge themes.

I would like to incorporate my logo and background images from my website (attached).

The advertisement should discretely near the firm name say "Offices: Brookvale"

The advertised words should be "Vectoring You Through Legal Turbulence"

The advertisement should also include my telephone number: "1-855-ROW-4738" and also my website "www.TheCounselDesk.com"

The call to action should say "Contact The Counsel Desk"

This is a Vertical Ad and its dimensions are 300x600 PX (72 DPI)

Must be in PNG or JPEG format.

Target Market(s)

Pilots/Aviation Enthusiasts

Industry/Entity Type

Law Firm

Font styles to use
Serif
Sans Serif

Colors
fbf289
fbed22
ffffff
1b1b1b
000000

Requirements
Must have
• The banner should definitely look professional, yet cutting edge. The banner definitely needs those things listed in the project description.
Nice to have
• Animation

```html
<!DOCTYPE html>
<html lang="en">
<head>
<meta charset="utf-8">
<title>The Marlow Law Firm – Vertical Banner</title>
<link rel="stylesheet" href="https://fonts.googleapis.com/css2?family=Cinzel:wght@600&family=Arimo:wght@500;700&family=Yellowtail&family=Playfair+Display:ital,wght@1,700&display=swap">
<style>
  :root {
    --gold-pale: #fbf289;
    --gold: #fbed22;
    --white: #ffffff;
    --charcoal: #1b1b1b;
    --black: #000000;
    --steel: #6f7276;
  }
  * { margin: 0; padding: 0; box-sizing: border-box; }
  html, body {
    width: 1200px;
    height: 2400px;
    overflow: hidden;
    background: var(--black);
  }
  .banner {
    position: relative;
    width: 1200px;
    height: 2400px;
    overflow: hidden;
    background: var(--black);
  }
  .hero-photo {
    position: absolute;
    left: 0;
    top: 760px;
    width: 1200px;
    height: 1640px;
    background:
      radial-gradient(ellipse 520px 440px at 600px 520px, #d8d9db 0%, #8d9094 45%, rgba(40,40,42,0) 100%),
      linear-gradient(180deg, #1b1b1b 0%, #3a3b3d 35%, #505154 60%, #2a2a2b 85%, #111 100%);
  }
  .runway-path {
    position: absolute;
    left: 0;
    top: 1400px;
    width: 1200px;
    height: 500px;
  }
  .masthead {
    position: absolute;
    left: 32px;
    top: 36px;
    width: 1136px;
    height: 190px;
  }
  .brand-mark {
    position: absolute;
    left: 0;
    top: 6px;
    width: 150px;
    height: 150px;
    border-radius: 50%;
    background: var(--gold);
  }
  .firm-name {
    position: absolute;
    left: 200px;
    top: 4px;
    width: 936px;
    text-align: center;
    font-family: "Cinzel", Georgia, serif;
    font-weight: 600;
    font-size: 68px;
    letter-spacing: 1px;
    color: var(--white);
  }
  .practice-areas {
    position: absolute;
    left: 200px;
    top: 124px;
    width: 936px;
    display: flex;
    align-items: center;
    gap: 18px;
    font-family: "Cinzel", Georgia, serif;
    font-weight: 600;
    font-size: 40px;
    color: var(--white);
    white-space: nowrap;
  }
  .practice-areas::before,
  .practice-areas::after {
    content: "";
    flex: 1;
    height: 4px;
    background: var(--white);
  }
  .office-line {
    position: absolute;
    left: 0;
    top: 230px;
    width: 1280px;
    text-align: center;
    font-family: "Yellowtail", cursive;
    font-size: 92px;
    color: var(--gold);
  }
  .headline {
    position: absolute;
    left: 60px;
    top: 360px;
    width: 1160px;
    text-align: center;
    font-family: "Arimo", Arial, sans-serif;
    font-weight: 500;
    font-size: 108px;
    line-height: 124px;
    color: var(--white);
    text-shadow: 6px 6px 10px rgba(0,0,0,0.85);
  }
  .cta {
    position: absolute;
    left: 348px;
    top: 1852px;
    width: 492px;
    height: 168px;
    border-radius: 22px;
    background: linear-gradient(180deg, var(--gold-pale) 0%, var(--gold) 55%, #e2c800 100%);
    border: 4px solid #fff8b0;
    display: flex;
    align-items: center;
    justify-content: center;
    font-family: "Playfair Display", Georgia, serif;
    font-style: italic;
    font-weight: 700;
    font-size: 80px;
    color: var(--charcoal);
  }
  .cta-name {
    position: absolute;
    left: 0;
    top: 2040px;
    width: 1200px;
    text-align: center;
    font-family: "Arimo", Arial, sans-serif;
    font-weight: 500;
    font-size: 56px;
    color: var(--white);
  }
  .phone {
    position: absolute;
    left: 0;
    top: 2130px;
    width: 1200px;
    display: flex;
    align-items: center;
    justify-content: center;
    gap: 20px;
    font-family: "Arimo", Arial, sans-serif;
    font-weight: 700;
    font-size: 96px;
    letter-spacing: 2px;
    color: var(--gold);
  }
  .phone-icon { width: 96px; height: 96px; }
  .web-address {
    position: absolute;
    left: 0;
    top: 2300px;
    width: 1200px;
    height: 100px;
    background: var(--charcoal);
    text-align: center;
    line-height: 100px;
    font-family: "Arimo", Arial, sans-serif;
    font-weight: 700;
    font-size: 50px;
    color: var(--white);
  }
</style>
</head>
<body>
<main class="banner">
  <div class="hero-photo" role="img" aria-label="Front view of a passenger jet parked on a night-lit airport apron"></div>

  <svg class="runway-path" viewBox="0 0 1200 500" aria-hidden="true">
    <path d="M0 380 C 300 300, 700 220, 1200 60" fill="none" stroke="var(--gold)" stroke-width="8" stroke-dasharray="34 22"/>
    <path d="M0 460 C 400 400, 800 300, 1200 160" fill="none" stroke="var(--gold)" stroke-width="8" stroke-dasharray="34 22"/>
  </svg>

  <header class="masthead">
    <span class="brand-mark" aria-hidden="true"></span>
    <h1 class="firm-name">The Marlow Law Firm</h1>
    <p class="practice-areas">Aviation Law | Drone Law</p>
  </header>

  <p class="office-line">Offices: Brookvale</p>

  <h2 class="headline">Vectoring You<br>Through Legal<br>Turbulence</h2>

  <a class="cta">Contact</a>
  <p class="cta-name">The Counsel Desk</p>

  <p class="phone">
    <svg class="phone-icon" viewBox="0 0 24 24" aria-hidden="true">
      <path fill="var(--gold)" d="M6.6 10.8a15.1 15.1 0 0 0 6.6 6.6l2.2-2.2c.3-.3.7-.4 1-.2 1.1.4 2.3.6 3.6.6.6 0 1 .4 1 1V20c0 .6-.4 1-1 1A17 17 0 0 1 3 4c0-.6.4-1 1-1h3.5c.6 0 1 .4 1 1 0 1.3.2 2.5.6 3.6.1.3 0 .7-.2 1z"/>
    </svg>
    1-855-ROW-4738
  </p>

  <p class="web-address">www.TheCounselDesk.com</p>
</main>
</body>
</html>
```